A Leisure SPA Plaza Hotel needs Creative VIP Cards Design

We need VIP Cards Design for a SPA Plaza Hotel, This leisure SPA plaza hotel have multiple sub projects, such as leisure hotel room, large buffet restaurant, swimming pool, theatrical performances, sauna bath, massage, SPA, Tea bar, 3D cinema, KTV rooms, chess room, Internet cafes , art appreciation, children's Castle, Korean geothermal, table tennis, billiard room, GYM and other entertainments.
We need Three creative VIP Card design for 3 different level:
1. Golden Card
2. Platinum Card
3. Diamond Card
Attached, Please find the LOGO file and some sample, we new design with much better look than those samples.

```html
<!DOCTYPE html>
<html lang="en">
<head>
<meta charset="utf-8">
<title>VIP Diamond Card</title>
<link rel="stylesheet" href="https://fonts.googleapis.com/css2?family=Open+Sans:wght@400;600&family=Raleway:wght@300;400&family=Cinzel:wght@500&display=swap">
<style>
  :root {
    --page-bg: #ffffff;
    --title-grey: #6f6f6f;
    --facet-light: #f4f4f4;
    --facet-mid: #c9c9c9;
    --facet-dark: #8d8d8d;
    --gold-light: #f7b733;
    --gold-mid: #f29a1f;
    --gold-deep: #c46f3a;
    --ink: #1e1a16;
    --text-dark: #222222;
    --signature-bar: #cdcdcd;
  }
  * { margin: 0; padding: 0; box-sizing: border-box; }
  html, body { width: 1200px; height: 960px; overflow: hidden; background: var(--page-bg); }
  .canvas { position: relative; width: 1200px; height: 960px; }

  .sheet-title { position: absolute; left: 92px; top: 74px; display: flex; align-items: flex-start; gap: 26px; color: var(--title-grey); }
  .sheet-title__vip { font-family: "Raleway", sans-serif; font-weight: 300; font-size: 46px; letter-spacing: 6px; line-height: 1; }
  .sheet-title__tier { font-family: "Raleway", sans-serif; font-weight: 400; font-size: 17px; letter-spacing: 3px; line-height: 20px; margin-top: 4px; }

  .card { position: absolute; left: 341px; width: 517px; height: 288px; overflow: hidden; box-shadow: 0 10px 14px -10px rgba(0,0,0,0.35); }
  .card--front { top: 122px; }
  .card--back { top: 533px; }
  .card__facets { position: absolute; inset: 0; background:
      linear-gradient(135deg, var(--facet-light) 0%, var(--facet-mid) 30%, var(--facet-light) 50%, var(--facet-dark) 72%, var(--facet-light) 100%); }
  .card--back .card__facets { background:
      linear-gradient(120deg, var(--facet-light) 0%, #dcdcdc 35%, var(--facet-light) 55%, #b9b9b9 80%, var(--facet-light) 100%); }

  .gold-plate { position: absolute; left: 153px; top: 39px; width: 210px; height: 211px;
    background: linear-gradient(160deg, var(--gold-light) 0%, var(--gold-mid) 45%, var(--gold-deep) 100%); }
  .gold-plate__frame { position: absolute; inset: 8px; border: 2px solid var(--ink); }
  .brand { position: absolute; left: 0; right: 0; top: 40px; display: flex; flex-direction: column; align-items: center; gap: 12px; color: var(--ink); }
  .brand__dot { width: 44px; height: 44px; border-radius: 50%; background: var(--ink); }
  .brand__name { font-family: "Open Sans", sans-serif; font-weight: 600; font-size: 14px; text-align: center; }
  .gold-plate__level { position: absolute; left: 0; right: 0; top: 136px; text-align: center; font-family: "Cinzel", serif; font-weight: 500; font-size: 26px; color: var(--ink); }
  .gold-plate__number { position: absolute; left: 0; right: 0; top: 168px; text-align: center; font-family: "Open Sans", sans-serif; font-size: 15px; letter-spacing: 2px; color: var(--ink); }

  .signature__label { position: absolute; left: 23px; top: 26px; font-family: "Open Sans", sans-serif; font-size: 21px; color: var(--text-dark); }
  .signature__bar { position: absolute; left: 20px; top: 59px; width: 369px; height: 40px; background: var(--signature-bar); }
  .terms { position: absolute; left: 53px; top: 131px; font-family: "Open Sans", sans-serif; font-size: 14px; line-height: 19px; color: var(--text-dark); }
  .terms p { margin-bottom: 18px; }
  .terms .terms__phone { margin-top: 24px; }
</style>
</head>
<body>
<main class="canvas">
  <header class="sheet-title">
    <span class="sheet-title__vip">VIP</span>
    <span class="sheet-title__tier">DIAMOND<br>CARD</span>
  </header>

  <section class="card card--front">
    <div class="card__facets" role="img" aria-label="Silver faceted diamond pattern background"></div>
    <div class="gold-plate">
      <div class="gold-plate__frame"></div>
      <div class="brand">
        <span class="brand__dot"></span>
        <span class="brand__name">Calder Stone Spa House</span>
      </div>
      <div class="gold-plate__level">VIP</div>
      <div class="gold-plate__number">No.00018</div>
    </div>
  </section>

  <section class="card card--back">
    <div class="card__facets" role="img" aria-label="Light silver faceted diamond pattern background"></div>
    <div class="signature__label">AUTHORIZE SIGNATURE</div>
    <div class="signature__bar"></div>
    <div class="terms">
      <p>Please show your membership card when you check out</p>
      <p>Signature and use of this card confirms the accecptance of the<br>Terms and Conditions of Membership</p>
      <p class="terms__phone">4001234567</p>
    </div>
  </section>
</main>
</body>
</html>
```